Calder Pizza - Takeout Menu Design

We are looking for a takeout menu design.
We are looking for a( 5" x 8.5" DOUBLE SIDED) flyer with our available pizza flavors
Must be easy to ready and not "busy"

Must include our logo (attached)
website: www.calderpizza.ca
address:
Fenwick Ridge Plaza
417, 318 9 Avenue SW
and the following details:
Visit our website for our complete appetizer, pasta, salad and catering menu.

Winner of this contest will also be offered to create a few print designs via printhive.

Please do not hesitate to ask any questions.

Target Market(s)

Business / Office clientele

Industry/Entity Type

Pizza place / specializing in corporate orders

Requirements
Must have
• Easy to read
Should not have
• Can not be busy or cluttered

```html
<!DOCTYPE html>
<html lang="en">
<head>
<meta charset="utf-8">
<title>Calder Pizza – Take-Out Menu</title>
<link rel="stylesheet" href="https://fonts.googleapis.com/css2?family=Open+Sans:ital,wght@0,400;0,600;0,700;1,400;1,700&display=swap">
<style>
  :root {
    --red: #c0281c;
    --ink: #1c1c1c;
    --rule: #d9d9d9;
    --paper: #ffffff;
    --stage: #2a2a2a;
    --crust: #d9a25a;
    --sauce: #b8452a;
  }
  * { box-sizing: border-box; margin: 0; padding: 0; }
  html, body { width: 775px; height: 1200px; overflow: hidden; }
  body { background: var(--stage); font-family: "Open Sans", Arial, sans-serif; color: var(--ink); position: relative; }

  .menu { position: absolute; left: 84px; top: 84px; width: 607px; height: 1031px; background: var(--paper); overflow: hidden; }

  .hero-photo { position: absolute; right: 0; top: 0; width: 240px; height: 300px; }

  .brand { position: absolute; left: 20px; top: 10px; display: flex; align-items: center; gap: 10px; }
  .brand-name { font-size: 50px; font-weight: 600; color: var(--red); letter-spacing: 0.5px; line-height: 1; }
  .brand-dot { width: 14px; height: 14px; border-radius: 50%; background: var(--red); }

  .web-bar { position: absolute; left: 20px; top: 71px; width: 368px; height: 21px; background: var(--red); color: #fff; font-size: 15px; font-weight: 600; letter-spacing: 2px; text-align: center; line-height: 21px; }

  .intro { position: absolute; left: 20px; top: 97px; width: 380px; font-size: 16px; line-height: 19px; }

  .size-tag { position: absolute; width: 57px; height: 23px; background: var(--red); color: #fff; font-weight: 700; font-size: 17px; text-align: center; line-height: 23px; }

  .section-title { position: absolute; color: var(--red); font-weight: 600; font-size: 19px; line-height: 24px; }

  .classic { position: absolute; left: 27px; top: 176px; width: 345px; }
  .classic-row { display: grid; grid-template-columns: 1fr 66px 54px; height: 17.7px; font-size: 12.5px; line-height: 17.7px; border-bottom: 1px solid var(--rule); }

  .specialty { position: absolute; left: 27px; top: 362px; width: 562px; }
  .pizza { display: grid; grid-template-columns: 1fr 66px 54px; height: 37px; border-bottom: 1px solid var(--rule); align-items: end; padding-bottom: 2px; }
  .pizza-name { font-weight: 700; font-size: 14px; line-height: 16px; }
  .pizza-desc { font-size: 12.5px; line-height: 16px; }
  .price { font-size: 12.5px; line-height: 16px; }

  .tax-note { position: absolute; right: 22px; top: 924px; font-size: 11px; font-style: italic; color: var(--red); }

  .footer { position: absolute; left: 0; bottom: 0; width: 607px; height: 84px; background: var(--red); color: #fff; }
  .footer-visit { position: absolute; left: 34px; top: 14px; width: 330px; font-size: 14.5px; font-weight: 700; font-style: italic; line-height: 19px; }
  .footer-address { position: absolute; left: 388px; top: 14px; display: flex; gap: 8px; font-size: 15px; line-height: 19px; }
  .pin { width: 14px; height: 20px; flex: none; }
</style>
</head>
<body>
  <main class="menu">
    <svg class="hero-photo" viewBox="0 0 240 300" role="img" aria-label="Photo of a fresh pepperoni and vegetable pizza">
      <defs>
        <radialGradient id="pizzaTone" cx="0.65" cy="0.35" r="0.8">
          <stop offset="0" stop-color="#c9573a"/>
          <stop offset="0.55" stop-color="var(--sauce)"/>
          <stop offset="1" stop-color="var(--crust)"/>
        </radialGradient>
      </defs>
      <path d="M0,0 H240 V280 C150,262 60,210 20,130 C8,90 0,45 0,0 Z" fill="url(#pizzaTone)"/>
      <path d="M0,150 C40,240 140,292 240,300 L240,280 C140,272 60,230 20,130 C12,140 5,146 0,150 Z" fill="#111"/>
    </svg>

    <div class="brand">
      <span class="brand-name">CALDER PIZZA</span>
      <span class="brand-dot"></span>
    </div>
    <div class="web-bar">www.calderpizza.ca</div>
    <p class="intro">All of our pizzas are prepared fresh everyday using only the finest mozzarella blend and ingredients.</p>

    <h2 class="section-title" style="left:14px; top:147px;">Classic Take-Out Pizza</h2>
    <div class="size-tag" style="left:243px; top:147px;">8"</div>
    <div class="size-tag" style="left:310px; top:147px;">13"</div>

    <div class="classic">
      <div class="classic-row"><span>Pepperoni &amp; Mushroom</span><span>$12.99</span><span>$30.95</span></div>
      <div class="classic-row"><span>Pepperoni</span><span>$11.99</span><span>$29.95</span></div>
      <div class="classic-row"><span>Hawaiian</span><span>$12.99</span><span>$30.95</span></div>
      <div class="classic-row"><span>Beef &amp; Mushroom</span><span>$13.49</span><span>$32.95</span></div>
      <div class="classic-row"><span>Pepperoni &amp; Ham</span><span>$12.99</span><span>$30.95</span></div>
      <div class="classic-row"><span>Ham &amp; Mushroom</span><span>$12.99</span><span>$30.95</span></div>
      <div class="classic-row"><span>Beef &amp; Onion</span><span>$13.49</span><span>$32.95</span></div>
      <div class="classic-row"><span>Cheese</span><span>$11.99</span><span>$29.95</span></div>
    </div>

    <h2 class="section-title" style="left:14px; top:337px;">Specialty Take-Out Pizza- 8" &amp; 13"</h2>
    <div class="size-tag" style="left:456px; top:337px;">8"</div>
    <div class="size-tag" style="left:520px; top:337px;">13"</div>

    <div class="specialty">
      <div class="pizza"><div><div class="pizza-name">All Meat</div><div class="pizza-desc">Pepperoni, Beef &amp; Smoked Ham &amp; Bacon</div></div><span class="price">$14.99</span><span class="price">$35.95</span></div>
      <div class="pizza"><div><div class="pizza-name">Double Pepperoni</div><div class="pizza-desc">Loads of Pepperoni</div></div><span class="price">$13.49</span><span class="price">$32.95</span></div>
      <div class="pizza"><div><div class="pizza-name">Hot Honey Pepperoni</div><div class="pizza-desc">Double Pepperoni and drizzled with Hot Honey</div></div><span class="price">$14.49</span><span class="price">$34.95</span></div>
      <div class="pizza"><div><div class="pizza-name">Hawaiian Heat</div><div class="pizza-desc">Smoked Ham, Pineapple and Banana Peppers</div></div><span class="price">$13.49</span><span class="price">$32.95</span></div>
      <div class="pizza"><div><div class="pizza-name">Four Cheese</div><div class="pizza-desc">Mozzarella, Feta, Romano and Cheddar Cheese</div></div><span class="price">$13.49</span><span class="price">$32.95</span></div>
      <div class="pizza"><div><div class="pizza-name">Montreal</div><div class="pizza-desc">Pepperoni &amp; Double Smoked Bacon</div></div><span class="price">$13.49</span><span class="price">$32.95</span></div>
      <div class="pizza"><div><div class="pizza-name">Montreal Heat</div><div class="pizza-desc">Pepperoni, Double Smoked Bacon &amp; Banana Peppers</div></div><span class="price">$13.99</span><span class="price">$33.95</span></div>
      <div class="pizza"><div><div class="pizza-name">Supreme</div><div class="pizza-desc">Pepperoni, Mushrooms &amp; Green Peppers</div></div><span class="price">$13.49</span><span class="price">$32.95</span></div>
      <div class="pizza"><div><div class="pizza-name">Canadian</div><div class="pizza-desc">Pepperoni, Mushrooms &amp; Ham</div></div><span class="price">$13.49</span><span class="price">$32.95</span></div>
      <div class="pizza"><div><div class="pizza-name">BBQ Chicken</div><div class="pizza-desc">Chicken Breast, Hickory BBQ Sauce &amp; Red Onions</div></div><span class="price">$13.99</span><span class="price">$33.95</span></div>
      <div class="pizza"><div><div class="pizza-name">BBQ Chicken Plus</div><div class="pizza-desc">Chicken Breast, Hickory BBQ Sauce, Red Onions &amp; Cilantro</div></div><span class="price">$14.79</span><span class="price">$34.95</span></div>
      <div class="pizza"><div><div class="pizza-name">Spicy BBQ Chicken</div><div class="pizza-desc">Chicken Breast, Hickory BBQ Sauce, Red Onions &amp; Banana Peppers</div></div><span class="price">$14.49</span><span class="price">$35.95</span></div>
      <div class="pizza"><div><div class="pizza-name">Sweet Chili Chicken</div><div class="pizza-desc">Chicken Breast, Pineapple, Red Onions &amp; Sweet Chili Sauce</div></div><span class="price">$14.49</span><span class="price">$35.95</span></div>
      <div class="pizza"><div><div class="pizza-name">Chicken Club</div><div class="pizza-desc">Chicken Breast, Double Smoked Bacon, Red Onions and Tomatoes</div></div><span class="price">$14.79</span><span class="price">$35.95</span></div>
      <div class="pizza"><div><div class="pizza-name">BBQ Pulled Pork</div><div class="pizza-desc">Pulled Pork, Red Onions, Red Peppers and Cilantro</div></div><span class="price">$14.49</span><span class="price">$35.95</span></div>
    </div>

    <p class="tax-note">GST not included</p>

    <footer class="footer">
      <p class="footer-visit">Visit our website www.calderpizza.ca for our complete appetizer, pasta, salad and catering menu.</p>
      <div class="footer-address">
        <svg class="pin" viewBox="0 0 14 20" aria-hidden="true">
          <path d="M7,0 C3.1,0 0,3.1 0,7 C0,12 7,20 7,20 C7,20 14,12 14,7 C14,3.1 10.9,0 7,0 Z M7,9.5 A2.5,2.5 0 1 1 7,4.5 A2.5,2.5 0 1 1 7,9.5 Z" fill="#fff"/>
        </svg>
        <p>Fenwick Ridge Plaza<br>417, 318 9 Avenue SW</p>
      </div>
    </footer>
  </main>
</body>
</html>
```